Coralbend Pastoral Traders Business Cards

We require business cards revamped with our logo. A few details we would like to use.

1. Round Edges
2. Our logo over the top of a wagyu cattle background photo on one side of the card

Other side of the card has the below details.

1. Person Name (First & Last)
2. Job Position
3. Mobile Number
4. Email Address
5. Website Address

Simple & Neat.

Target Market(s)

Sales

Industry/Entity Type

Agriculture

Contact Information for Business Card

CORALBEND PASTORAL TRADERS

Colors

Designer to choose colors to be used in the design.

Requirements
Must have
• Company Logo

```html
<!DOCTYPE html>
<html lang="en">
<head>
<meta charset="utf-8">
<title>Coralbend Pastoral Traders – Business Cards</title>
<link rel="stylesheet" href="https://fonts.googleapis.com/css2?family=Poppins:wght@400;500;600;700&display=swap">
<style>
  :root {
    --stage: #222222;
    --card-dark: #1c1c1d;
    --card-dark-edge: #262628;
    --brand-red: #a3161c;
    --brand-red-bright: #c41c22;
    --brand-wine: #5c0b22;
    --brand-logo-dim: #6e1020;
    --text-light: #f2f2f2;
    --pattern-deep: #6e1117;
    --pattern-mid: #8e161c;
    --pattern-bright: #b81c22;
  }
  * { box-sizing: border-box; margin: 0; padding: 0; }
  html, body { width: 1200px; height: 780px; overflow: hidden; }
  body {
    background: var(--stage);
    font-family: "Poppins", sans-serif;
    position: relative;
  }
  .card {
    position: absolute;
    top: 241px;
    width: 520px;
    height: 298px;
    border-radius: 22px;
    overflow: hidden;
    box-shadow: 0 18px 40px rgba(0,0,0,.55);
  }

  /* Contact side */
  .card--contact {
    left: 45px;
    background: linear-gradient(135deg, var(--card-dark-edge), var(--card-dark));
  }
  .contact__wordmark {
    position: absolute;
    left: 30px;
    top: 34px;
    width: 210px;
    font-weight: 600;
    font-size: 21px;
    line-height: 1.15;
    color: var(--brand-logo-dim);
  }
  .contact__divider {
    position: absolute;
    left: 0; top: 0;
    width: 520px; height: 298px;
  }
  .contact__person {
    position: absolute;
    left: 290px;
    top: 70px;
  }
  .contact__name {
    font-size: 28px;
    line-height: 1.1;
    color: var(--brand-red);
    white-space: nowrap;
  }
  .contact__name .first { font-weight: 700; }
  .contact__name .last { font-weight: 400; }
  .contact__role {
    margin-top: 4px;
    font-size: 14px;
    font-weight: 500;
    color: var(--text-light);
  }
  .contact__list {
    list-style: none;
    margin-top: 14px;
  }
  .contact__item {
    display: flex;
    align-items: center;
    gap: 8px;
    font-size: 12.5px;
    color: var(--text-light);
    line-height: 1.75;
    white-space: nowrap;
  }
  .contact__icon { width: 13px; height: 13px; flex: none; }
  .contact__band {
    position: absolute;
    left: 0; bottom: 0;
    width: 100%;
    height: 24px;
    background: linear-gradient(90deg, var(--brand-red) 0 88%, var(--brand-wine) 88% 100%);
  }
  .contact__address {
    position: absolute;
    left: 30px;
    top: 4px;
    font-size: 12px;
    color: var(--text-light);
    white-space: nowrap;
  }

  /* Brand side */
  .card--brand { left: 635px; }
  .brand__pattern {
    position: absolute;
    inset: 0;
    background:
      radial-gradient(circle at 85% 80%, var(--pattern-bright), transparent 55%),
      linear-gradient(135deg, var(--pattern-deep), var(--pattern-mid));
  }
  .brand__wordmark {
    position: absolute;
    left: 0; right: 0;
    top: 50%;
    transform: translateY(-50%);
    text-align: center;
    font-weight: 600;
    font-size: 30px;
    line-height: 1.15;
    color: var(--text-light);
  }
</style>
</head>
<body>

  <section class="card card--contact" aria-label="Business card, contact side">
    <div class="contact__wordmark">Coralbend Pastoral Traders</div>

    <svg class="contact__divider" viewBox="0 0 520 298" aria-hidden="true">
      <line x1="150" y1="230" x2="290" y2="60" stroke="var(--brand-red)" stroke-width="1" opacity=".7"/>
    </svg>

    <div class="contact__person">
      <h1 class="contact__name"><span class="first">Marta</span> <span class="last">Velkova</span></h1>
      <p class="contact__role">Founder &amp; CEO</p>
      <ul class="contact__list">
        <li class="contact__item">
          <svg class="contact__icon" viewBox="0 0 24 24" aria-hidden="true"><path fill="var(--brand-red-bright)" d="M6.6 10.8a15.1 15.1 0 0 0 6.6 6.6l2.2-2.2a1 1 0 0 1 1-.25 11.4 11.4 0 0 0 3.6.57 1 1 0 0 1 1 1V20a1 1 0 0 1-1 1A17 17 0 0 1 3 4a1 1 0 0 1 1-1h3.5a1 1 0 0 1 1 1c0 1.25.2 2.45.57 3.57a1 1 0 0 1-.25 1z"/></svg>
          (555) 214-6083
        </li>
        <li class="contact__item">
          <svg class="contact__icon" viewBox="0 0 24 24" aria-hidden="true"><rect x="2" y="5" width="20" height="14" rx="2" fill="var(--brand-red-bright)"/><path d="M3 6l9 7 9-7" fill="none" stroke="var(--card-dark)" stroke-width="2"/></svg>
          info@coralbendpastoral.com
        </li>
        <li class="contact__item">
          <svg class="contact__icon" viewBox="0 0 24 24" aria-hidden="true"><circle cx="12" cy="12" r="10" fill="var(--brand-red-bright)"/><path d="M2 12h20M12 2c3 3 3 17 0 20M12 2c-3 3-3 17 0 20" fill="none" stroke="var(--card-dark)" stroke-width="1.5"/></svg>
          www.coralbendpastoral.com
        </li>
      </ul>
    </div>

    <div class="contact__band">
      <p class="contact__address">1740 Harrow Creek Rd. Suite 310 Denton, TX 76201</p>
    </div>
  </section>

  <section class="card card--brand" aria-label="Business card, brand side">
    <div class="brand__pattern" role="img" aria-label="Embossed repeating brand pattern in deep red tones"></div>
    <div class="brand__wordmark">Coralbend<br>Pastoral Traders</div>
  </section>

</body>
</html>
```